Scrubbing Paper Towel Company needs Label Design

We need a product label that wraps around a roll of scrubbing paper towels as a sticker label of individually wrapped rolls. The sticker label has dimensions of 11.5" x 6" (width x height). The company logo with the brand feel and color theme is attached.

This is mainly used for dishwashing. A very large section of the label should show dishwashing and cleaning. Two very similar products can be found here :
---> https://www.shopvarnel.example/Non-Scratch-Disposable-Dish-Washing-Scrubbing-KT47M/dp/Q5283LRTVN/ref=sr_1_9?keywords=scouring+sheet&qid=2840175396&sr=8-9
--->https://www.shopvarnel.example/Zuvi-Flair-Disposable-Dish-washing-Scrubbing/dp/Q3961HWPXT/ref=sr_1_15?keywords=scouring+sheet&qid=2840175396&sr=8-15

To be included in the label:

Key points:
Did you know? Sponges are the perfect place for bacteria growth! We're talking hundreds of different species of bacteria growing in your dishwashing sponge - just as bad as the inside of your toilet. So why use a dirty sponge over and over again? Why does it smell so bad? Yes your toilet is gross, but why should the sponge go overlooked?

The Brisko Roll is a sanitary solution to this problem. Use it once, wash and reuse up to three times before throwing each sheet away - that's enough for 180 washes per roll! But don't limit yourself to dishwashing. It's great for scrubbing surfaces with hardened debris or even dry residue left from old spills. So go ahead, take a stand against bacteria and wash away knowing your kitchen is finally clean. Now that's sanitary!

Multipurpose Use:
Dishwashing
**(with example image/graphic)**
Cleaning Toilets
Cleaning Grills
Wiping Down Stoves
Cleaning Sinks
Cleaning Pet Bowls

60 Sheets
7.9" X 8.7" per sheet

Features:
Perforated for Easy Tear
Reusable
Liquid Absorbent
Non-Flammable
Cadmium Free
Kitchen Safe

```html
<!DOCTYPE html>
<html lang="en">
<head>
<meta charset="utf-8">
<title>Brisko Roll – Wrap Label</title>
<link rel="stylesheet" href="https://fonts.googleapis.com/css2?family=Montserrat:wght@500;600;700;800&family=Kaushan+Script&display=swap">
<style>
  :root {
    --page: #ffffff;
    --navy-deep: #27307a;
    --navy: #2f3f94;
    --blue-mid: #4a74bf;
    --blue-light: #6fa3da;
    --white: #ffffff;
    --yellow: #f5d51e;
    --divider: rgba(255,255,255,0.25);
    --scene-light: #e8f1d8;
    --scene-mid: #b9d2cf;
    --scene-dark: #6f95b8;
  }
  * { margin: 0; padding: 0; box-sizing: border-box; }
  html, body {
    width: 1200px; height: 1200px; overflow: hidden;
    background: var(--page);
  }
  .canvas { position: relative; width: 1200px; height: 1200px; }

  .label {
    position: absolute; left: 25px; top: 300px;
    width: 1150px; height: 600px; overflow: hidden;
    background: radial-gradient(ellipse 38% 62% at 50% 48%, var(--blue-light) 0%, var(--blue-mid) 40%, var(--navy) 78%, var(--navy-deep) 100%);
    font-family: "Montserrat", sans-serif;
    color: var(--white);
  }
  .feature-line {
    position: absolute; top: 14px; left: 0; right: 0;
    text-align: center; white-space: nowrap;
    font-weight: 500; font-size: 15px; letter-spacing: 0.2px;
  }

  .panel {
    position: absolute; top: 52px; bottom: 24px;
  }
  .panel-story { left: 30px; width: 340px; }
  .panel-front { left: 380px; width: 390px; }
  .panel-uses { left: 790px; width: 330px; padding-left: 22px; border-left: 1px solid var(--divider); }
  .panel-story { padding-right: 20px; border-right: 1px solid var(--divider); }

  .panel-heading {
    font-family: "Kaushan Script", cursive;
    font-weight: 400; font-size: 30px; color: var(--yellow);
    margin-bottom: 8px;
  }
  .story-copy {
    font-size: 12.5px; font-weight: 500; line-height: 1.42;
    margin-bottom: 10px;
  }
  .story-copy strong { font-weight: 700; color: var(--yellow); }

  .brand-name {
    position: absolute; left: 0; right: 0; top: 70px;
    text-align: center; font-weight: 800; line-height: 0.95;
  }
  .brand-name .word-main { display: block; font-size: 90px; letter-spacing: -2px; }
  .brand-name .word-sub { display: block; font-size: 52px; letter-spacing: 3px; margin-top: 4px; padding-left: 90px; }
  .tagline {
    position: absolute; left: 60px; top: 258px;
    font-family: "Kaushan Script", cursive;
    font-size: 26px; white-space: nowrap;
    transform: rotate(-8deg); transform-origin: left center;
  }
  .hero-visual {
    position: absolute; left: 20px; top: 290px;
    width: 350px; height: 230px;
  }

  .use-visual {
    display: block; width: 300px; height: 96px; margin: 4px 0 12px;
  }
  .use-list { list-style: none; margin-bottom: 18px; }
  .use-item {
    display: flex; align-items: center; gap: 10px;
    font-size: 16px; font-weight: 600; line-height: 1.75;
  }
  .use-item svg { width: 18px; height: 18px; flex: none; }
  .sheet-info {
    border-top: 1px solid var(--divider); padding-top: 12px;
  }
  .sheet-count { font-size: 34px; font-weight: 800; color: var(--yellow); line-height: 1; }
  .sheet-size { font-size: 16px; font-weight: 600; margin-top: 6px; }
</style>
</head>
<body>
<div class="canvas">
  <section class="label">
    <p class="feature-line">Perforated for Easy Tear / Reusable / Liquid Absorbent / Non-Flammable / Cadmium Free / Kitchen Safe</p>

    <div class="panel panel-story">
      <h2 class="panel-heading">Did you know?</h2>
      <p class="story-copy">Sponges are the perfect place for bacteria growth! We're talking hundreds of different species of bacteria growing in your dishwashing sponge - just as bad as the inside of your toilet. So why use a dirty sponge over and over again? Why does it smell so bad? Yes your toilet is gross, but why should the sponge go overlooked?</p>
      <p class="story-copy">The Brisko Roll is a sanitary solution to this problem. Use it once, wash and reuse up to three times before throwing each sheet away - that's enough for <strong>180 washes per roll!</strong> But don't limit yourself to dishwashing. It's great for scrubbing surfaces with hardened debris or even dry residue left from old spills. So go ahead, take a stand against bacteria and wash away knowing your kitchen is finally clean. <strong>Now that's sanitary!</strong></p>
    </div>

    <div class="panel panel-front">
      <h1 class="brand-name">
        <span class="word-main">Brisko</span>
        <span class="word-sub">ROLL</span>
      </h1>
      <p class="tagline">Clean Smarter, Not Harder</p>
      <svg class="hero-visual" viewBox="0 0 560 340" role="img" aria-label="Photo of a hand wiping a stack of white plates with a yellow scrubbing sheet, surrounded by soap bubbles">
        <defs>
          <linearGradient id="sceneFill" x1="0" y1="0" x2="1" y2="1">
            <stop offset="0" stop-color="var(--scene-dark)"/>
            <stop offset="0.35" stop-color="var(--scene-light)"/>
            <stop offset="0.7" stop-color="var(--scene-mid)"/>
            <stop offset="1" stop-color="var(--scene-dark)"/>
          </linearGradient>
        </defs>
        <path d="M20 210 C10 120 150 55 330 40 C470 28 545 60 540 140 C535 230 470 300 330 318 C180 336 30 300 20 210 Z"
              fill="url(#sceneFill)" stroke="var(--yellow)" stroke-width="12"/>
      </svg>
    </div>

    <div class="panel panel-uses">
      <h2 class="panel-heading">Multipurpose Use</h2>
      <svg class="use-visual" viewBox="0 0 300 96" role="img" aria-label="Photo of dishes being washed with a yellow scrubbing sheet">
        <defs>
          <linearGradient id="useFill" x1="0" y1="0" x2="1" y2="1">
            <stop offset="0" stop-color="var(--scene-light)"/>
            <stop offset="1" stop-color="var(--scene-dark)"/>
          </linearGradient>
        </defs>
        <rect x="2" y="2" width="296" height="92" rx="14" fill="url(#useFill)" stroke="var(--yellow)" stroke-width="4"/>
      </svg>
      <ul class="use-list">
        <li class="use-item"><svg viewBox="0 0 18 18"><circle cx="9" cy="9" r="9" fill="var(--yellow)"/><path d="M5 9.5l2.6 2.6L13 6.5" fill="none" stroke="var(--navy-deep)" stroke-width="2.2" stroke-linecap="round" stroke-linejoin="round"/></svg>Dishwashing</li>
        <li class="use-item"><svg viewBox="0 0 18 18"><circle cx="9" cy="9" r="9" fill="var(--yellow)"/><path d="M5 9.5l2.6 2.6L13 6.5" fill="none" stroke="var(--navy-deep)" stroke-width="2.2" stroke-linecap="round" stroke-linejoin="round"/></svg>Cleaning Toilets</li>
        <li class="use-item"><svg viewBox="0 0 18 18"><circle cx="9" cy="9" r="9" fill="var(--yellow)"/><path d="M5 9.5l2.6 2.6L13 6.5" fill="none" stroke="var(--navy-deep)" stroke-width="2.2" stroke-linecap="round" stroke-linejoin="round"/></svg>Cleaning Grills</li>
        <li class="use-item"><svg viewBox="0 0 18 18"><circle cx="9" cy="9" r="9" fill="var(--yellow)"/><path d="M5 9.5l2.6 2.6L13 6.5" fill="none" stroke="var(--navy-deep)" stroke-width="2.2" stroke-linecap="round" stroke-linejoin="round"/></svg>Wiping Down Stoves</li>
        <li class="use-item"><svg viewBox="0 0 18 18"><circle cx="9" cy="9" r="9" fill="var(--yellow)"/><path d="M5 9.5l2.6 2.6L13 6.5" fill="none" stroke="var(--navy-deep)" stroke-width="2.2" stroke-linecap="round" stroke-linejoin="round"/></svg>Cleaning Sinks</li>
        <li class="use-item"><svg viewBox="0 0 18 18"><circle cx="9" cy="9" r="9" fill="var(--yellow)"/><path d="M5 9.5l2.6 2.6L13 6.5" fill="none" stroke="var(--navy-deep)" stroke-width="2.2" stroke-linecap="round" stroke-linejoin="round"/></svg>Cleaning Pet Bowls</li>
      </ul>
      <div class="sheet-info">
        <p class="sheet-count">60 Sheets</p>
        <p class="sheet-size">7.9" X 8.7" per sheet</p>
      </div>
    </div>
  </section>
</div>
</body>
</html>
```